Nonna's Vellato

I am looking to design a label to be used on a glass jar for packaging a very special spice that has been used in our family for generations. The spice is excellent on meats, burgers, poultry, fish, and more.

The name of the spice is "Nonna's Famous Vellato"

Design should be traditional, with an Italian feel.

Total circumference of the jar is 10"
Height of jar is 4"

Some of the glass should not be covered to reveal color of spice inside.

Target Market(s)

Female 25-75

```html
<!DOCTYPE html>
<html lang="en">
<head>
<meta charset="utf-8">
<title>Nonna's Famous Vellato – Jar Label</title>
<link rel="stylesheet" href="https://fonts.googleapis.com/css2?family=Cookie&family=Mali:wght@500&display=swap">
<style>
  :root {
    --page: #ffffff;
    --band-red: #a51c1f;
    --band-edge: #1a1a1a;
    --ink-white: #ffffff;
  }
  html, body {
    margin: 0;
    padding: 0;
    width: 1200px;
    height: 900px;
    overflow: hidden;
    background: var(--page);
  }
  .canvas {
    position: relative;
    width: 1200px;
    height: 900px;
    background: var(--page);
    overflow: hidden;
  }
  .label-band {
    position: absolute;
    left: 0;
    top: 327px;
    width: 1200px;
    height: 245px;
    background: var(--band-red);
    border-top: 1.5px solid var(--band-edge);
    border-bottom: 1.5px solid var(--band-edge);
    box-sizing: border-box;
  }
  .product-name {
    margin: 0;
    font-weight: 500;
  }
  .product-initial {
    position: absolute;
    left: 140px;
    top: 228px;
    font-family: "Mali", sans-serif;
    font-weight: 500;
    font-size: 360px;
    line-height: 1;
    color: var(--ink-white);
  }
  .brand-line {
    position: absolute;
    left: 470px;
    top: 372px;
    font-family: "Cookie", cursive;
    font-size: 62px;
    font-weight: 400;
    line-height: 1;
    color: var(--ink-white);
  }
  .product-rest {
    position: absolute;
    left: 385px;
    top: 450px;
    font-family: "Mali", sans-serif;
    font-weight: 500;
    font-size: 108px;
    line-height: 1;
    letter-spacing: 24px;
    color: var(--ink-white);
  }
  .shaker-art {
    position: absolute;
    left: 866px;
    top: 336px;
    width: 212px;
    height: 212px;
  }
</style>
</head>
<body>
  <main class="canvas">
    <div class="label-band"></div>

    <h1 class="product-name" aria-label="Nonna's Famous Vellato">
      <span class="brand-line">Nonna's Famous</span>
      <span class="product-initial" aria-hidden="true">V</span>
      <span class="product-rest" aria-hidden="true">ellato</span>
    </h1>

    <svg class="shaker-art" role="img" aria-label="Illustration of a spice shaker sprinkling white seasoning" viewBox="0 0 212 212">
      <defs>
        <linearGradient id="shakerTone" x1="1" y1="0" x2="0" y2="1">
          <stop offset="0" stop-color="#ffffff" stop-opacity="0.35"/>
          <stop offset="1" stop-color="#ffffff" stop-opacity="0.12"/>
        </linearGradient>
      </defs>
      <rect x="0" y="0" width="212" height="212" rx="16" fill="url(#shakerTone)"/>
    </svg>
  </main>
</body>
</html>
```